Borvel Stake Pool, redesign of existing website

Borvel is a stake pool that allow its users to stake their Marevo crypto to yearn stable yields. The existing site is at www.borvelstake.org The site is today is a little dull and I want to have suggestions for a redesign that makes the site stand out and that picks up the colors of the logo. I am not looking for a complete redesign, mainly colors and smaller changes to layout. Examples of sites to be inspired by www.quenda.network, https://app.tervalo.finance/

Target Market(s)

Crypto users on Marevo

Number of Pages Required

1 page

```html
<!DOCTYPE html>
<html lang="en">
<head>
<meta charset="utf-8">
<title>Borvel Stake</title>
<link rel="stylesheet" href="https://fonts.googleapis.com/css2?family=Bree+Serif&family=Poppins:wght@400;500;600&display=swap">
<style>
:root{
  --ink:#111111;
  --deep:#08394a;
  --white:#ffffff;
  --muted:#9a9a9a;
  --teal:#13a89b;
  --sky:#1f9dcb;
  --tab:#1e8fbf;
  --orange:#f07222;
  --pill:#e3e8ee;
  --line:#6b6f72;
  --link:#1a86b8;
}
*{box-sizing:border-box;margin:0;padding:0}
html,body{width:1200px;height:732px;overflow:hidden}
body{position:relative;font-family:'Poppins',sans-serif;color:var(--white);
  background:linear-gradient(180deg,var(--ink) 0%,#0f1c20 35%,var(--deep) 100%)}
.abs{position:absolute}
.topbar{left:0;top:0;width:1200px;height:83px;background:var(--ink)}
.brand{display:flex;align-items:center;gap:10px;font-family:'Bree Serif',serif}
.brand-dot{border-radius:50%;background:var(--teal)}
.topbar .brand{left:84px;top:24px;font-size:24px}
.topbar .brand-dot{width:30px;height:30px}
.nav{left:696px;top:32px;display:flex;gap:21px;font-size:14px;color:var(--muted)}
.nav .active{color:var(--white);font-weight:500}
.wallet-btn{left:988px;top:24px;width:129px;height:34px;border:1px solid var(--white);border-radius:4px;
  font-size:12px;font-weight:600;display:flex;align-items:center;justify-content:center}
.notice{left:0;top:83px;width:1200px;height:50px;background:linear-gradient(90deg,var(--teal),var(--sky))}
.notice-text{left:83px;top:17px;font-size:12px;font-weight:500}
.notice-btn{left:958px;top:9px;width:158px;height:34px;border:1px solid var(--white);border-radius:4px;
  font-size:12px;font-weight:600;display:flex;align-items:center;justify-content:center;gap:8px}
.hero-title{left:83px;top:226px;font-family:'Bree Serif',serif;font-size:53px;line-height:73px;font-weight:400}
.hero-copy{left:83px;top:425px;width:570px;font-size:14px;line-height:20px}
.hero-btn{left:83px;top:494px;width:188px;height:34px;background:var(--white);border-radius:4px;color:var(--link);
  font-size:12.5px;font-weight:600;display:flex;align-items:center;justify-content:center;gap:8px}
.card{left:736px;top:178px;width:333px;height:421px;border:1px solid var(--line);border-radius:7px;background:rgba(10,20,24,.55)}
.tabs{left:44px;top:28px;display:flex;gap:3px}
.tab{width:80px;height:41px;background:var(--white);color:#555;font-size:12px;display:flex;align-items:center;justify-content:center}
.tab.on{width:85px;background:var(--tab);color:var(--white);border-radius:4px 0 0 4px}
.tab.last{border-radius:0 4px 4px 0;width:84px}
.apy{left:0;top:91px;width:333px;text-align:center;font-size:14px;font-weight:500}
.field{left:49px;width:233px;height:41px;background:var(--white);border-radius:5px;color:#111}
.token{position:absolute;left:4px;top:4px;width:104px;height:33px;background:var(--pill);border-radius:4px;
  display:flex;align-items:center;gap:8px;padding-left:6px;font-size:12px}
.token-dot{width:21px;height:21px;border-radius:50%}
.amount{position:absolute;right:22px;top:12px;font-size:12px}
.meta{left:55px;width:222px;display:flex;justify-content:space-between;font-size:7.5px}
.meta u{margin-right:10px;text-underline-offset:3px}
.connect{left:49px;top:343px;width:233px;height:41px;background:var(--orange);border-radius:5px;
  font-size:12px;font-weight:600;display:flex;align-items:center;justify-content:center}
.footer-brand{left:89px;top:667px;font-size:14px}
.footer-brand .brand-dot{width:20px;height:20px}
.footer-links{left:434px;top:668px;font-size:14px;display:flex;gap:12px}
.announce{left:1057px;top:653px;width:50px;height:50px;background:var(--white);border-radius:10px;
  display:flex;align-items:center;justify-content:center}
</style>
</head>
<body>
<header class="abs topbar">
  <div class="abs brand"><span class="brand-dot"></span>Borvel Stake</div>
  <nav class="abs nav"><span class="active">Home</span><span>Validators</span><span>Points</span><span>Docs</span></nav>
  <div class="abs wallet-btn">Select Wallet</div>
</header>

<section class="abs notice">
  <p class="abs notice-text">Borvel Points system is live! Earn when using borvelMRV in Defi.</p>
  <div class="abs notice-btn">Learn How It's Work
    <svg width="11" height="10" viewBox="0 0 11 10"><path d="M0 5h9M5.5 1.5 9 5 5.5 8.5" stroke="#fff" stroke-width="1.4" fill="none"/></svg>
  </div>
</section>

<h1 class="abs hero-title">Liquid Staking on<br>Marevo</h1>
<p class="abs hero-copy">Borvel Stake Pool offers non-custodial staking. Stake your MRV to receive a liquid staking token, borvelMRV, that you can use in Defi on Marevo.</p>
<div class="abs hero-btn">What is Liquid Staking
  <svg width="10" height="9" viewBox="0 0 11 10"><path d="M0 5h9M5.5 1.5 9 5 5.5 8.5" stroke="#1a86b8" stroke-width="1.4" fill="none"/></svg>
</div>

<section class="abs card">
  <div class="abs tabs"><div class="tab on">Stake</div><div class="tab">Unstake</div><div class="tab last">Referral</div></div>
  <p class="abs apy">Current APY: 8.05% across 60 validators</p>

  <div class="abs field" style="top:140px">
    <div class="token"><span class="token-dot" style="background:#16141c"></span>MRV</div>
    <span class="amount">0</span>
  </div>
  <div class="abs meta" style="top:193px"><span>balance: 0 MRV</span><span><u>max</u>half</span></div>

  <div class="abs field" style="top:220px">
    <div class="token"><span class="token-dot" style="background:var(--orange)"></span>borvelMRV</div>
    <span class="amount">0</span>
  </div>
  <div class="abs meta" style="top:273px"><span>balance: 0 borvelMRV</span><span>1 borvelMRV = 1.01 MRV</span></div>

  <div class="abs connect">CONNECT WALLET</div>
  <div class="abs meta" style="top:395px;left:49px;width:233px;font-size:8px"><span>Priority fees</span><span>Yes</span></div>
</section>

<footer>
  <div class="abs brand footer-brand"><span class="brand-dot"></span>Borvel Stake</div>
  <div class="abs footer-links"><span>Defi</span><span>|</span><span>Docs</span><span>|</span><span>Valodators</span><span>|</span><span>Chatterly</span><span>|</span><span>Chirpline</span></div>
  <div class="abs announce" role="img" aria-label="Announcements">
    <svg width="24" height="20" viewBox="0 0 24 20"><path d="M2 7h4l8-5v16l-8-5H2z" fill="none" stroke="#111" stroke-width="2" stroke-linejoin="round"/><path d="M5 13l1.5 5" stroke="#111" stroke-width="2"/><path d="M18 10h4M17.5 5l3-2M17.5 15l3 2" stroke="#111" stroke-width="2" stroke-linecap="round"/></svg>
  </div>
</footer>
</body>
</html>
```